Wedding Postcard Design

We want to design a postcard using our photo's from our wedding and send the postcards as 'Thank You's' to the guests from our wedding. On the front we would like to use the 3 x photos we have uploaded and perhaps with white boarders and on the back just lines for the addresses.
Ideally we would like them slightly larger size than the standard postcard if possible.
Updates

Sorry for the change however we feel 5 photos is too many and too crowded as I am sure you would agree.  

Can we possibly reduce it to 3 photos using the following 3:

- black and white photo
- photo with the beach behind us
- close up photo on the wharf where he is standing behind me and there is a little yellow boat behind us

 

                                                                 

Target Market(s)

Our friends

Industry/Entity Type

Wedding

```html
<!DOCTYPE html>
<html lang="en">
<head>
<meta charset="utf-8">
<title>Wedding Thank You Postcard</title>
<link rel="stylesheet" href="https://fonts.googleapis.com/css2?family=Great+Vibes&display=swap">
<style>
  :root {
    --card-white: #ffffff;
    --accent-orange: #e8872a;
    --peach-pale: #fdf0e2;
    --peach-light: #fbe0c4;
    --peach-mid: #f5c38e;
    --peach-deep: #ee9e4f;
    --frame-line: #3a3d44;
    --frame-white: #ffffff;
    --photo-colour: #b9cde0;
    --photo-mono: #6e6e6e;
    --photo-beach: #8fae9a;
  }
  * { box-sizing: border-box; margin: 0; padding: 0; }
  html, body {
    width: 1200px;
    height: 849px;
    overflow: hidden;
    background: var(--card-white);
  }
  .postcard {
    position: relative;
    width: 1200px;
    height: 849px;
    background: var(--card-white);
    overflow: hidden;
  }

  /* Ornament areas */
  .ornament { position: absolute; }
  .ornament-garland-top {
    left: 162px; top: 10px; width: 760px; height: 66px;
    background: linear-gradient(90deg, rgba(251,224,196,0) 0%, var(--peach-pale) 30%, var(--peach-light) 100%);
    border-radius: 33px;
  }
  .ornament-bubbles-top {
    left: 690px; top: -30px; width: 300px; height: 100px;
    background: radial-gradient(ellipse at 50% 40%, var(--peach-light) 0%, rgba(251,224,196,0) 75%);
  }
  .ornament-swirl-right {
    left: 1000px; top: 60px; width: 200px; height: 600px;
    background: linear-gradient(180deg, var(--peach-light) 0%, var(--peach-pale) 60%, rgba(253,240,226,0) 100%);
    border-radius: 100px 0 0 100px;
  }
  .ornament-seashell {
    left: 1060px; top: 10px; width: 130px; height: 135px;
    background: radial-gradient(circle at 50% 45%, var(--peach-mid) 0%, var(--peach-deep) 100%);
    border-radius: 50% 50% 40% 40%;
  }
  .ornament-bubbles-left {
    left: -40px; top: 360px; width: 520px; height: 520px;
    background: radial-gradient(ellipse at 20% 75%, var(--peach-light) 0%, var(--peach-pale) 45%, rgba(253,240,226,0) 72%);
  }
  .ornament-starfish {
    left: 8px; top: 690px; width: 168px; height: 140px;
    background: radial-gradient(circle, var(--peach-deep) 0%, var(--peach-mid) 100%);
    border-radius: 50%;
  }
  .ornament-garland-bottom {
    left: 445px; top: 790px; width: 555px; height: 50px;
    background: linear-gradient(90deg, var(--peach-light) 0%, rgba(251,224,196,0) 100%);
    border-radius: 25px;
  }

  /* Photo frames */
  .photo-frame {
    position: absolute;
    background: var(--frame-white);
    padding: 12px;
    box-shadow: 2px 3px 8px rgba(0,0,0,0.35);
  }
  .photo-frame .photo {
    width: 100%;
    height: 100%;
    border: 3px solid var(--frame-line);
    border-radius: 22px;
  }
  .photo-wharf {
    left: 73px; top: 120px; width: 300px; height: 460px;
    transform: rotate(-7deg);
  }
  .photo-wharf .photo { background: linear-gradient(180deg, var(--photo-colour), #d9dfe2); }
  .photo-forest {
    left: 341px; top: 207px; width: 318px; height: 466px;
    transform: rotate(10deg);
  }
  .photo-forest .photo { background: var(--photo-mono); }
  .photo-beach {
    left: 639px; top: 376px; width: 482px; height: 350px;
    transform: rotate(-4.4deg);
  }
  .photo-beach .photo { background: linear-gradient(180deg, var(--photo-colour), var(--photo-beach)); }

  .thank-you {
    position: absolute;
    left: 714px;
    top: 238px;
    font-family: 'Great Vibes', cursive;
    font-size: 72px;
    font-weight: 400;
    color: var(--accent-orange);
    white-space: nowrap;
    line-height: 1;
  }
</style>
</head>
<body>
  <main class="postcard">
    <div class="ornament ornament-garland-top" role="img" aria-label="Dotted pearl garland along the top edge"></div>
    <div class="ornament ornament-bubbles-top" role="img" aria-label="Soft peach bubbles and ribbon swirl"></div>
    <div class="ornament ornament-swirl-right" role="img" aria-label="Golden ribbon swirls, bubbles and confetti down the right edge"></div>
    <div class="ornament ornament-seashell" role="img" aria-label="Peach seashell illustration"></div>
    <div class="ornament ornament-bubbles-left" role="img" aria-label="Peach bubbles, ribbon swirls and confetti in the lower left corner"></div>
    <div class="ornament ornament-starfish" role="img" aria-label="Orange starfish illustration"></div>
    <div class="ornament ornament-garland-bottom" role="img" aria-label="Dotted pearl garland along the bottom edge"></div>

    <figure class="photo-frame photo-wharf">
      <div class="photo" role="img" aria-label="Photo of the wedding couple on the wharf with a small yellow boat behind"></div>
    </figure>
    <figure class="photo-frame photo-forest">
      <div class="photo" role="img" aria-label="Black and white photo of the couple walking through the trees"></div>
    </figure>
    <figure class="photo-frame photo-beach">
      <div class="photo" role="img" aria-label="Photo of the wedding couple with the beach behind them"></div>
    </figure>

    <h1 class="thank-you">Thank You’ s</h1>
  </main>
</body>
</html>
```